Lumex.CI Portal Application Design

** See the attached treatment PDF document with complete details, but here are the broad points:**

We need designs for a login screen and three very similar interior page screens. Because the app requires a CodeNest, RepoKeep or Stackpail account to login, screen shots are attached to this treatment. Please review those for the designs needed.
- Login Page
- Project Index page (with sidebar tabs for other options. Those specific pages do not need to be coded once we have the template).
- Project build list. A list of the builds available per project
- Build details. This shows the build steps and results of the build steps.

The site should be visually compatible with https://lumexweb.example-host.net. The same logo and color scheme (logo attached)

General templates are desired that we can build on.

There is a significant bonus tip involved if you’re willing to provide a toggle for a light and a dark mode. I do not know what this would look like but feel free to present proposals.

Industry/Entity Type

Continuous Integration/Testing (think LoopForge, KestrelCI)

Coding

Coded - Design and coding required

Number of Pages Required

1 page

Font styles to use
Sans Serif
Other font styles liked:
• Roboto

Colors
0054AA
0677BA
7BADD7
CADEEF
E8F1F8
FFC000
F8CF3A
FAE287
FDF2CF
FEFAEE

Requirements
Nice to have
• Light and Dark Mode

```html
<!DOCTYPE html>
<html lang="en">
<head>
<meta charset="utf-8">
<title>Lumex.CI – Projects, dark and light modes</title>
<link rel="stylesheet" href="https://fonts.googleapis.com/css2?family=Nunito+Sans:wght@400;600;700&display=swap">
<style>
  :root{
    --canvas:#d5dce6;
    --accent:#14c8b0;
    --star:#f5c518;
  }
  *{box-sizing:border-box;margin:0;padding:0}
  html,body{width:1200px;height:1200px;overflow:hidden;background:var(--canvas);font-family:"Nunito Sans",sans-serif}
  .screen{position:absolute;left:183px;width:792px;height:543px;overflow:hidden;background:var(--main-bg);color:var(--text)}
  .screen.dark{
    top:45px;
    --side-bg:#161a21;--side-text:#e6e9ef;--side-muted:#9aa3b2;--side-line:#262b34;--side-active:#2a2f39;
    --main-bg:#1c2029;--header-bg:#1c2029;--header-line:#2c313b;
    --text:#eef1f5;--muted:#a6afbd;--card-bg:#222731;--card-line:#343a45;
    --btn-bg:#272c36;--btn-line:#363c47;--btn-text:#eef1f5;--toggle-on:#4a6a9a;
    --field-bg:#1c2029;--field-line:#3a404b;--upgrade:#8493ab;--star-box:#3b3521;--star-off:#8d9ab0;
    --pub-bg:transparent;--menu-bg:#232833;
  }
  .screen.light{
    top:612px;
    --side-bg:#0e1230;--side-text:#eef0fa;--side-muted:#a3a9c6;--side-line:#1e2447;--side-active:#262b48;
    --main-bg:#f6f8fb;--header-bg:#ffffff;--header-line:#e6e9ef;
    --text:#1d222c;--muted:#5f6775;--card-bg:#ffffff;--card-line:#e4e7ed;
    --btn-bg:#ffffff;--btn-line:#e1e5eb;--btn-text:#1d222c;--toggle-on:#e9edf3;
    --field-bg:#ffffff;--field-line:#dfe3e9;--upgrade:#3b4054;--star-box:#fdf5d3;--star-off:#8d9ab0;
    --pub-bg:#f5f7fa;--menu-bg:#ffffff;
  }
  /* sidebar */
  .sidebar{position:absolute;left:0;top:0;width:196px;height:100%;background:var(--side-bg);color:var(--side-text)}
  .brand{position:absolute;left:15px;top:15px;display:flex;align-items:center;gap:9px;font-size:16px;font-weight:600}
  .brand-mark{width:23px;height:23px;border-radius:50%;background:#8a93a6}
  .side-line{position:absolute;left:0;width:196px;height:1px;background:var(--side-line)}
  .repo-select{position:absolute;left:14px;top:67px;width:166px;height:28px;border:1px solid #4a5160;border-radius:5px;font-size:10px;padding-left:12px;line-height:26px;color:var(--side-text)}
  .repo-select svg{position:absolute;right:7px;top:10px}
  .side-scroll{position:absolute;left:190px;top:106px;width:4px;height:272px;border-radius:2px;background:#3a404c}
  .nav-label{position:absolute;left:15px;font-size:9px;letter-spacing:.5px;color:var(--side-muted);font-weight:600}
  .nav-item{position:absolute;left:0;width:188px;height:33px;display:flex;align-items:center;gap:9px;padding-left:17px;font-size:11px}
  .nav-item.active{background:var(--side-active);border-left:3px solid #6b7384;padding-left:14px}
  .nav-item svg{width:12px;height:12px;fill:var(--side-text)}
  .storage{position:absolute;left:15px;top:468px;width:166px;font-size:11px;display:flex;justify-content:space-between}
  .storage-bar{position:absolute;left:15px;top:487px;width:166px;height:4px;border-radius:2px;background:#4a5060}
  .storage-bar span{display:block;width:3px;height:100%;border-radius:2px;background:#9aa4b6}
  .upgrade{position:absolute;left:14px;top:500px;width:166px;height:28px;border-radius:5px;background:var(--upgrade);color:#fff;font-size:10.5px;font-weight:600;display:flex;align-items:center;justify-content:center;gap:6px}
  /* header */
  .topbar{position:absolute;left:196px;top:0;width:596px;height:57px;background:var(--header-bg);border-bottom:1px solid var(--header-line)}
  .page-title{position:absolute;left:25px;top:16px;font-size:18px;font-weight:600}
  .search{position:absolute;left:320px;top:12px;width:212px;height:32px;border:1px solid var(--field-line);background:var(--field-bg);border-radius:5px;font-size:10.5px;color:var(--muted);display:flex;align-items:center;gap:9px;padding-left:9px}
  .avatar{position:absolute;border-radius:50%;background:linear-gradient(150deg,#c9ccd1,#6b6f76)}
  .main-scroll{position:absolute;left:788px;top:63px;width:3px;height:385px;border-radius:2px;background:#3a404b}
  .light .main-scroll{background:#cfd5de}
  /* page head */
  .heading{position:absolute;left:221px;top:82px;font-size:21px;font-weight:600}
  .subheading{position:absolute;left:221px;top:113px;font-size:10.5px;color:var(--muted)}
  .btn{position:absolute;top:89px;height:32px;border:1px solid var(--btn-line);background:var(--btn-bg);color:var(--btn-text);border-radius:4px;display:flex;align-items:center;justify-content:center;gap:6px;font-size:11px;font-weight:600}
  .btn svg{fill:currentColor}
  .view-toggle{position:absolute;top:89px;left:519px;width:58px;height:32px;border:1px solid var(--btn-line);border-radius:4px;display:flex;overflow:hidden;background:var(--btn-bg)}
  .view-toggle span{flex:1;display:flex;align-items:center;justify-content:center;color:var(--btn-text)}
  .view-toggle span.on{background:var(--toggle-on)}
  .btn.primary{background:var(--accent);border-color:var(--accent);color:#fff}
  /* cards */
  .card{position:absolute;width:262px;height:261px;background:var(--card-bg);border:1px solid var(--card-line);border-radius:6px;overflow:hidden}
  .card .shot{position:absolute;left:0;top:0;width:100%;height:122px}
  .card .shot.tall{height:200px}
  .name{position:absolute;left:15px;top:136px;font-size:14px;font-weight:600}
  .repo{position:absolute;left:15px;top:158px;font-size:10px;color:var(--muted);display:flex;align-items:center;gap:5px}
  .repo i{width:9px;height:9px;border-radius:50%;border:1.5px solid var(--muted)}
  .stat{position:absolute;top:180px;font-size:11px;font-weight:600}
  .stat small{display:block;font-size:8.5px;font-weight:400;letter-spacing:.6px;color:var(--muted);margin-top:1px}
  .published{position:absolute;left:15px;top:220px;width:232px;height:25px;border-radius:4px;background:var(--pub-bg);font-size:10.5px;display:flex;align-items:center;gap:7px;padding-left:10px}
  .published i{width:6px;height:6px;border-radius:50%;background:var(--accent)}
  .star-box{position:absolute;left:221px;top:137px;width:24px;height:24px;border-radius:4px;background:var(--star-box);display:flex;align-items:center;justify-content:center}
  .star-plain{position:absolute;left:227px;top:141px}
  /* menus */
  .filter-menu{position:absolute;left:503px;top:128px;width:151px;height:120px;background:var(--menu-bg);border:1px solid #343a45;border-radius:5px;box-shadow:0 6px 18px rgba(0,0,0,.35)}
  .menu-row{position:absolute;left:15px;display:flex;align-items:center;gap:9px;font-size:11px;color:var(--text)}
  .menu-row svg{width:11px;height:11px;fill:currentColor}
  .menu-row.dim{color:var(--muted)}
  .profile-menu{position:absolute;left:558px;top:50px;width:211px;height:349px;background:var(--menu-bg);border:1px solid #e4e7ed;border-radius:5px;box-shadow:0 8px 22px rgba(20,30,50,.14)}
  .profile-name{position:absolute;left:57px;top:16px;font-size:12.5px;font-weight:600}
  .profile-mail{position:absolute;left:57px;top:34px;font-size:9.5px;color:var(--muted)}
  .menu-line{position:absolute;left:12px;width:186px;height:1px;background:#e6e9ef}
  .profile-menu .menu-row{left:22px;gap:10px}
  .profile-menu .menu-row svg{fill:#7a8291}
  .switch{position:absolute;left:155px;top:194px;width:34px;height:18px;border-radius:9px;background:#e4e7ec;border:1px solid #d8dce3}
  .switch i{position:absolute;left:2px;top:2px;width:12px;height:12px;border-radius:50%;background:#fff;box-shadow:0 1px 2px rgba(0,0,0,.2)}
</style>
</head>
<body>

<svg width="0" height="0" style="position:absolute">
  <defs>
    <symbol id="i-star" viewBox="0 0 20 20"><path d="M10 1l2.7 5.9 6.3.7-4.7 4.3 1.3 6.3L10 15l-5.6 3.2 1.3-6.3L1 7.6l6.3-.7z"/></symbol>
    <symbol id="i-moon" viewBox="0 0 20 20"><path d="M12 2a8 8 0 1 0 6 13A7 7 0 0 1 12 2z"/></symbol>
    <symbol id="i-list" viewBox="0 0 20 20"><rect x="1" y="3" width="3" height="2.5"/><rect x="6" y="3" width="13" height="2.5"/><rect x="1" y="9" width="3" height="2.5"/><rect x="6" y="9" width="13" height="2.5"/><rect x="1" y="15" width="3" height="2.5"/><rect x="6" y="15" width="13" height="2.5"/></symbol>
    <symbol id="i-grid" viewBox="0 0 20 20"><path d="M2 2h16v16H2z M4 4v5h5V4z M11 4v5h5V4z M4 11v5h5v-5z M11 11v5h5v-5z" fill-rule="evenodd"/></symbol>
    <symbol id="i-funnel" viewBox="0 0 20 20"><path d="M1 2h18l-7 8v8l-4-2v-6z"/></symbol>
    <symbol id="i-plus" viewBox="0 0 20 20"><path d="M9 2h2v7h7v2h-7v7H9v-7H2V9h7z"/></symbol>
    <symbol id="i-tree" viewBox="0 0 20 20"><rect x="1" y="2" width="7" height="5"/><rect x="12" y="2" width="7" height="5"/><rect x="7" y="13" width="7" height="5"/><path d="M5 7h2v3h6V7h2v5H5z"/></symbol>
    <symbol id="i-box" viewBox="0 0 20 20"><path d="M10 1l8 4v10l-8 4-8-4V5zm0 2.3L4.5 6 10 8.7 15.5 6z"/></symbol>
    <symbol id="i-key" viewBox="0 0 20 20"><circle cx="13" cy="7" r="5"/><path d="M9 10l-7 7 2 2 2-2 1 1 2-2-1-1 3-3z"/></symbol>
    <symbol id="i-team" viewBox="0 0 20 20"><circle cx="6" cy="6" r="3"/><circle cx="14" cy="6" r="3"/><path d="M0 16c0-4 3-6 6-6s6 2 6 6zM10 16c0-2 1-4 2-5 4 0 8 1 8 5z"/></symbol>
    <symbol id="i-shield" viewBox="0 0 20 20"><path d="M10 1l8 3v6c0 5-4 8-8 9-4-1-8-4-8-9V4z"/></symbol>
    <symbol id="i-chart" viewBox="0 0 20 20"><path d="M2 2h2v14h15v2H2z"/><rect x="6" y="9" width="2" height="6"/><rect x="10" y="5" width="2" height="10"/><rect x="14" y="11" width="2" height="4"/></symbol>
    <symbol id="i-rocket" viewBox="0 0 20 20"><path d="M18 2c-5 0-9 3-11 7l4 4c4-2 7-6 7-11zM6 10l-4 1 3 2zM10 14l-1 4 -2-3zM4 14c-2 1-2 4-2 4s3 0 4-2z"/></symbol>
    <symbol id="i-search" viewBox="0 0 20 20"><path d="M8 2a6 6 0 1 1 0 12A6 6 0 0 1 8 2zm0 2a4 4 0 1 0 0 8 4 4 0 0 0 0-8zm4.5 8.5l1.5-1.5 5 5-1.5 1.5z"/></symbol>
    <symbol id="i-layers" viewBox="0 0 20 20"><path d="M10 2l9 4-9 4-9-4zM1 10l2-1 7 3 7-3 2 1-9 4zM1 14l2-1 7 3 7-3 2 1-9 4z"/></symbol>
    <symbol id="i-play" viewBox="0 0 20 20"><path d="M10 1a9 9 0 1 1 0 18 9 9 0 0 1 0-18zM8 6v8l6-4z" fill-rule="evenodd"/></symbol>
    <symbol id="i-sync" viewBox="0 0 20 20"><path d="M10 3a7 7 0 0 1 6.3 4H19l-3.5 4L12 7h2a5 5 0 0 0-9 1H3a7 7 0 0 1 7-5zM1 9l3.5 4L8 9H6a5 5 0 0 0 9 3h2a7 7 0 0 1-13 1H1z"/></symbol>
    <symbol id="i-user" viewBox="0 0 20 20"><circle cx="10" cy="6" r="4.5"/><path d="M2 19c0-5 4-7 8-7s8 2 8 7z"/></symbol>
    <symbol id="i-gear" viewBox="0 0 20 20"><path d="M8.5 1h3l.5 2.5 2 1 2.2-1.4 2.1 2.1-1.4 2.2.9 2.1L19 10v0l0 1.5-2.5.5-.9 2 1.4 2.2-2.1 2.1-2.2-1.4-2 .9L11.5 19h-3L8 16.5l-2-.9-2.2 1.4-2.1-2.1L3 12.7 2 10.5 1 10V8.5L3.5 8l.9-2L3 3.8 5.1 1.7 7.3 3.1l1-.5zM10 7a3 3 0 1 0 0 6 3 3 0 0 0 0-6z" fill-rule="evenodd"/></symbol>
    <symbol id="i-bell" viewBox="0 0 20 20"><path d="M10 1c3.5 0 6 2.5 6 6v5l2 3H2l2-3V7c0-3.5 2.5-6 6-6zM7.5 16.5h5a2.5 2.5 0 0 1-5 0z"/></symbol>
    <symbol id="i-palette" viewBox="0 0 20 20"><path d="M10 1a9 9 0 0 0 0 18c1.5 0 2-1 1.5-2-.6-1.2.2-2.5 1.6-2.5H15a4 4 0 0 0 4-4C19 5 15 1 10 1zM5 10a1.5 1.5 0 1 1 0-3 1.5 1.5 0 0 1 0 3zm3-4a1.5 1.5 0 1 1 0-3 1.5 1.5 0 0 1 0 3zm5 0a1.5 1.5 0 1 1 0-3 1.5 1.5 0 0 1 0 3z" fill-rule="evenodd"/></symbol>
    <symbol id="i-help" viewBox="0 0 20 20"><path d="M10 1a9 9 0 1 1 0 18 9 9 0 0 1 0-18zm-.8 12.5v2h1.8v-2zM10 4.5c-2 0-3.3 1.2-3.4 3h1.9c.1-.8.6-1.3 1.5-1.3s1.4.5 1.4 1.2c0 1.5-2.5 1.5-2.5 4h1.8c0-1.8 2.6-2 2.6-4.2 0-1.6-1.3-2.7-3.3-2.7z" fill-rule="evenodd"/></symbol>
    <symbol id="i-exit" viewBox="0 0 20 20"><path d="M2 2h8v2H4v12h6v2H2zM13 5l5 5-5 5v-3.5H7v-3h6z"/></symbol>
    <symbol id="i-chevron" viewBox="0 0 10 6"><path d="M1 1l4 4 4-4" fill="none" stroke="currentColor" stroke-width="1.6"/></symbol>
  </defs>
</svg>

<!-- ============ DARK MODE ============ -->
<section class="screen dark">
  <aside class="sidebar">
    <div class="brand"><span class="brand-mark"></span>Lumex.CI</div>
    <div class="side-line" style="top:56px"></div>
    <div class="repo-select">LumexCI/lumex.ci<svg width="9" height="6"><use href="#i-chevron"/></svg></div>
    <div class="side-line" style="top:106px"></div>
    <div class="side-scroll"></div>
    <div class="nav-label" style="top:167px;top:168px"></div>
    <div class="nav-label" style="top:168px;display:none"></div>
    <div class="nav-label" style="top:168px"></div>
    <div class="nav-label" style="top:168px"></div>
    <div class="nav-label" style="top:122px">MAIN</div>
    <div class="nav-item active" style="top:185px;top:140px"><svg><use href="#i-tree"/></svg>Projects</div>
    <div class="nav-item" style="top:173px"><svg><use href="#i-list"/></svg>Builds</div>
    <div class="nav-item" style="top:207px"><svg><use href="#i-box"/></svg>Build Assets</div>
    <div class="nav-item" style="top:240px"><svg><use href="#i-key"/></svg>Upload Tokens</div>
    <div class="nav-label" style="top:292px">TEAM</div>
    <div class="nav-item" style="top:310px"><svg><use href="#i-team"/></svg>Team Members</div>
    <div class="nav-item" style="top:343px"><svg><use href="#i-shield"/></svg>Permissions</div>
    <div class="nav-label" style="top:396px">ACCOUNT</div>
    <div class="nav-item" style="top:413px"><svg><use href="#i-chart"/></svg>Analytics</div>
    <div class="side-line" style="top:451px"></div>
    <div class="storage"><span>Storage</span><span>8.72 GB / 900 GB</span></div>
    <div class="storage-bar"><span></span></div>
    <div class="upgrade"><svg width="11" height="11" fill="#fff"><use href="#i-rocket"/></svg>Upgrade Now</div>
  </aside>

  <header class="topbar">
    <h1 class="page-title">Projects</h1>
    <div class="search"><svg width="13" height="13" fill="currentColor"><use href="#i-search"/></svg>Search projects...</div>
    <div class="avatar" role="img" aria-label="User profile photo" style="left:542px;top:14px;width:28px;height:28px"></div>
  </header>
  <div class="main-scroll"></div>

  <h2 class="heading">Your Projects</h2>
  <p class="subheading">Manage and deploy your projects with ease</p>
  <div class="btn" style="left:436px;width:73px"><svg width="10" height="10"><use href="#i-moon"/></svg>Theme</div>
  <div class="view-toggle"><span class="on"><svg width="11" height="11" fill="currentColor"><use href="#i-grid"/></svg></span><span><svg width="11" height="11" fill="currentColor"><use href="#i-list"/></svg></span></div>
  <div class="btn" style="left:587px;width:67px"><svg width="11" height="11"><use href="#i-funnel"/></svg>Filter</div>
  <div class="btn primary" style="left:664px;width:100px"><svg width="10" height="10"><use href="#i-plus"/></svg>New Project</div>

  <article class="card" style="left:221px;top:146px">
    <div class="shot" role="img" aria-label="Photo of a laptop screen showing code" style="background:linear-gradient(160deg,#3a3f48 0%,#1b2a44 45%,#0f1626 100%)"></div>
    <div class="name">lumex-ci</div>
    <div class="repo"><i></i>LumexCI/lumex.ci</div>
    <div class="stat" style="left:15px">main<small>BRANCH</small></div>
    <div class="stat" style="left:65px">42<small>BUILDS</small></div>
    <div class="published"><i></i>Published • 2 hours ago</div>
    <div class="star-box"><svg width="11" height="11" fill="var(--star)"><use href="#i-star"/></svg></div>
  </article>

  <article class="card" style="left:502px;top:146px">
    <div class="shot" role="img" aria-label="Photo of an analytics dashboard on a monitor" style="background:linear-gradient(120deg,#0e1318 0%,#0f2a30 50%,#1a5f6a 75%,#e8ecef 100%)"></div>
    <div class="name">lumex-docs</div>
    <div class="repo"><i></i>LumexCI/documentation</div>
    <div class="stat" style="left:15px">main<small>BRANCH</small></div>
    <div class="stat" style="left:65px">18<small>BUILDS</small></div>
    <div class="published"><i></i>Published • 1 day ago</div>
    <svg class="star-plain" width="11" height="11" fill="var(--star-off)"><use href="#i-star"/></svg>
  </article>

  <article class="card" style="left:221px;top:426px">
    <div class="shot tall" role="img" aria-label="Photo of a hand holding a phone with a weather app" style="background:linear-gradient(140deg,#e4e8ee 0%,#b9c2cf 45%,#6b7a8c 75%,#2e343b 100%)"></div>
  </article>
  <article class="card" style="left:502px;top:426px">
    <div class="shot tall" role="img" aria-label="Photo of a smartphone home screen with app icons" style="background:linear-gradient(135deg,#8fa6b0 0%,#5d7f8e 40%,#c26a6a 75%,#7aa7cf 100%)"></div>
  </article>

  <div class="filter-menu">
    <div class="menu-row dim" style="top:14px"><svg><use href="#i-layers"/></svg>All Projects</div>
    <div class="menu-row" style="top:41px"><svg><use href="#i-play"/></svg>Active</div>
    <div class="menu-row" style="top:68px"><svg><use href="#i-star"/></svg>Favorites</div>
    <div class="menu-row" style="top:95px"><svg><use href="#i-sync"/></svg>Building</div>
  </div>
</section>

<!-- ============ LIGHT MODE ============ -->
<section class="screen light">
  <aside class="sidebar">
    <div class="brand"><span class="brand-mark"></span>Lumex.CI</div>
    <div class="side-line" style="top:56px"></div>
    <div class="repo-select">LumexCI/lumex.ci<svg width="9" height="6"><use href="#i-chevron"/></svg></div>
    <div class="side-line" style="top:106px"></div>
    <div class="side-scroll"></div>
    <div class="nav-label" style="top:122px">MAIN</div>
    <div class="nav-item active" style="top:140px"><svg><use href="#i-tree"/></svg>Projects</div>
    <div class="nav-item" style="top:173px"><svg><use href="#i-list"/></svg>Builds</div>
    <div class="nav-item" style="top:207px"><svg><use href="#i-box"/></svg>Build Assets</div>
    <div class="nav-item" style="top:240px"><svg><use href="#i-key"/></svg>Upload Tokens</div>
    <div class="nav-label" style="top:292px">TEAM</div>
    <div class="nav-item" style="top:310px"><svg><use href="#i-team"/></svg>Team Members</div>
    <div class="nav-item" style="top:343px"><svg><use href="#i-shield"/></svg>Permissions</div>
    <div class="nav-label" style="top:396px">ACCOUNT</div>
    <div class="nav-item" style="top:413px"><svg><use href="#i-chart"/></svg>Analytics</div>
    <div class="side-line" style="top:451px"></div>
    <div class="storage"><span>Storage</span><span>8.72 GB / 900 GB</span></div>
    <div class="storage-bar"><span></span></div>
    <div class="upgrade"><svg width="11" height="11" fill="#fff"><use href="#i-rocket"/></svg>Upgrade Now</div>
  </aside>

  <header class="topbar">
    <h1 class="page-title">Projects</h1>
    <div class="search"><svg width="13" height="13" fill="currentColor"><use href="#i-search"/></svg>Search projects...</div>
    <div class="avatar" role="img" aria-label="User profile photo" style="left:542px;top:14px;width:28px;height:28px"></div>
  </header>
  <div class="main-scroll"></div>

  <h2 class="heading">Your Projects</h2>
  <p class="subheading">Manage and deploy your projects with ease</p>
  <div class="btn" style="left:436px;width:73px"><svg width="10" height="10"><use href="#i-moon"/></svg>Theme</div>
  <div class="view-toggle"><span><svg width="11" height="11" fill="currentColor"><use href="#i-grid"/></svg></span><span class="on" style="background:#3b4054"></span></div>

  <article class="card" style="left:221px;top:146px">
    <div class="shot" role="img" aria-label="Photo of a laptop screen showing code" style="background:linear-gradient(160deg,#3a3f48 0%,#1b2a44 45%,#0f1626 100%)"></div>
    <div class="name">lumex-ci</div>
    <div class="repo"><i></i>LumexCI/lumex.ci</div>
    <div class="stat" style="left:15px">main<small>BRANCH</small></div>
    <div class="stat" style="left:65px">42<small>BUILDS</small></div>
    <div class="published"><i></i>Published • 2 hours ago</div>
    <div class="star-box"><svg width="11" height="11" fill="var(--star)"><use href="#i-star"/></svg></div>
  </article>

  <article class="card" style="left:502px;top:146px">
    <div class="shot" role="img" aria-label="Photo of an analytics dashboard on a monitor" style="background:linear-gradient(120deg,#1d2a22 0%,#0f1a2c 40%,#1c4f8f 70%,#0e1420 100%)"></div>
    <div class="name">lumex-docs</div>
    <div class="repo"><i></i>LumexCI/documentation</div>
    <div class="stat" style="left:15px">main<small>BRANCH</small></div>
    <div class="stat" style="left:65px">18<small>BUILDS</small></div>
    <div class="published"><i></i>Published • 1 day ago</div>
  </article>

  <article class="card" style="left:221px;top:426px">
    <div class="shot tall" role="img" aria-label="Photo of a hand holding a phone with a weather app" style="background:linear-gradient(140deg,#e4e8ee 0%,#b9c2cf 45%,#6b7a8c 75%,#2e343b 100%)"></div>
  </article>
  <article class="card" style="left:502px;top:426px">
    <div class="shot tall" role="img" aria-label="Photo of a smartphone home screen with app icons" style="background:linear-gradient(135deg,#8fa6b0 0%,#5d7f8e 40%,#c26a6a 75%,#7aa7cf 100%)"></div>
  </article>

  <div class="profile-menu">
    <div class="avatar" role="img" aria-label="User profile photo" style="left:12px;top:12px;width:36px;height:36px"></div>
    <div class="profile-name">Avery Coder</div>
    <div class="profile-mail">avery.coder@example.com</div>
    <div class="menu-line" style="top:60px"></div>
    <div class="menu-row" style="top:78px"><svg><use href="#i-user"/></svg>Profile Settings</div>
    <div class="menu-row" style="top:111px"><svg><use href="#i-gear"/></svg>Account Preferences</div>
    <div class="menu-row" style="top:144px"><svg><use href="#i-bell"/></svg>Notification Settings</div>
    <div class="menu-line" style="top:176px"></div>
    <div class="menu-row" style="top:195px"><svg><use href="#i-moon"/></svg>Dark Mode</div>
    <div class="switch"><i></i></div>
    <div class="menu-row" style="top:230px"><svg><use href="#i-palette"/></svg>Theme Customization</div>
    <div class="menu-line" style="top:262px"></div>
    <div class="menu-row" style="top:279px"><svg><use href="#i-help"/></svg>Help &amp; Support</div>
    <div class="menu-row" style="top:312px"><svg><use href="#i-exit"/></svg>Sign Out</div>
  </div>
</section>

</body>
</html>
```